Velvet Paw Hospital Business Card Design

I need a business card designed for my cat only veterinary clinic. I will upload the logo that I would like included on the card. Please include:
Business Name: The Velvet Paw Hospital
Address: 20947 E. 38th St, Scottsdale, AZ 85371
Phone #: 480-555-6143
Website URL: www.velvetpawvets.com
And the Doctors Name: Marisol Brenn, DVM

```html
<!DOCTYPE html>
<html lang="en">
<head>
<meta charset="utf-8">
<title>The Velvet Paw Hospital – Business Card</title>
<link rel="stylesheet" href="https://fonts.googleapis.com/css2?family=Quicksand:wght@400&family=Ubuntu:wght@400;700&display=swap">
<style>
  :root {
    --backdrop: #e9e7e4;
    --card-grey: #4e4e50;
    --rule-dark: #2c2c2e;
    --ink: #1f1e20;
    --paper: #ffffff;
    --paper-shade: #e4e4e4;
    --accent-blue: #3d86c6;
    --mark-fill: #231a2a;
  }
  * { box-sizing: border-box; margin: 0; padding: 0; }
  html, body { width: 1200px; height: 900px; overflow: hidden; }
  body {
    background: var(--backdrop);
    position: relative;
    font-family: "Ubuntu", sans-serif;
  }
  .card {
    position: absolute;
    left: 250px;
    width: 700px;
    height: 400px;
    overflow: hidden;
    box-shadow: 0 6px 18px rgba(0,0,0,0.18);
  }
  .brand-mark {
    border-radius: 50%;
    background: var(--mark-fill);
  }
  /* Back side */
  .card--back { top: 35px; background: var(--card-grey); }
  .back-brand {
    position: absolute; left: 0; right: 0; top: 60px;
    display: flex; flex-direction: column; align-items: center; gap: 14px;
  }
  .back-brand .brand-mark { width: 120px; height: 120px; }
  .back-brand .brand-name {
    font-family: "Quicksand", sans-serif;
    font-weight: 400;
    font-size: 20px;
    color: var(--rule-dark);
  }
  .site-line {
    position: absolute; left: 150px; right: 150px; top: 265px;
    text-align: center;
    font-family: "Quicksand", sans-serif;
    font-size: 15px;
    letter-spacing: 0.42em;
    color: var(--rule-dark);
    padding-bottom: 14px;
    border-bottom: 1px solid var(--rule-dark);
  }
  /* Front side */
  .card--front {
    top: 465px;
    background: linear-gradient(100deg, var(--paper) 0%, var(--paper-shade) 55%, var(--paper) 100%);
  }
  .card--front .brand-mark {
    position: absolute; left: 40px; top: 40px;
    width: 165px; height: 165px;
  }
  .clinic-name {
    position: absolute; left: 222px; top: 56px;
    font-family: "Quicksand", sans-serif;
    font-weight: 400;
    font-size: 34px; line-height: 1.05;
    color: var(--ink);
  }
  .clinic-name span { display: block; padding-left: 26px; }
  .doctor-name {
    position: absolute; left: 150px; top: 222px;
    font-size: 34px; font-weight: 700; color: var(--ink);
  }
  .doctor-name small { font-size: 26px; font-weight: 400; }
  .contact-band {
    position: absolute; left: 0; right: 0; bottom: 0; height: 120px;
    background: var(--ink);
    color: var(--paper);
  }
  .contact-list {
    position: absolute; left: 150px; top: 24px;
    list-style: none; font-size: 20px; line-height: 32px;
  }
  .contact-list li, .address { display: flex; align-items: flex-start; gap: 12px; }
  .contact-list svg, .address svg { flex: none; margin-top: 7px; }
  .address {
    position: absolute; left: 400px; top: 22px;
    font-size: 20px; line-height: 30px;
  }
  .address p span { display: block; padding-left: 14px; }
  .corner-figure {
    position: absolute; right: 22px; bottom: 60px;
    width: 120px; height: 165px;
    border-radius: 50px 50px 8px 8px;
    background: var(--ink);
    outline: 3px solid var(--paper);
    outline-offset: -6px;
  }
</style>
</head>
<body>
  <section class="card card--back" aria-label="Card back">
    <div class="back-brand">
      <div class="brand-mark" aria-hidden="true"></div>
      <p class="brand-name">Velvet Paw Hospital</p>
    </div>
    <p class="site-line">www.velvetpawvets.com</p>
  </section>

  <section class="card card--front" aria-label="Card front">
    <div class="brand-mark" aria-hidden="true"></div>
    <h1 class="clinic-name">The Velvet<span>Paw Hospital</span></h1>
    <h2 class="doctor-name">Marisol Brenn, <small>DVM</small></h2>
    <div class="corner-figure" role="img" aria-label="Decorative seated cat silhouette"></div>
    <div class="contact-band">
      <ul class="contact-list">
        <li>
          <svg width="20" height="18" viewBox="0 0 20 18" aria-hidden="true"><path d="M2 6c0-3 4-4 8-4s8 1 8 4l-3 1-1-2H6L5 7 2 6z M4 9h12l1 7H3z" fill="var(--accent-blue)"/></svg>
          480-555-6143
        </li>
        <li>
          <svg width="20" height="20" viewBox="0 0 20 20" aria-hidden="true"><circle cx="10" cy="10" r="8" fill="none" stroke="var(--accent-blue)" stroke-width="2"/><path d="M2 10h16M10 2c-4 4-4 12 0 16M10 2c4 4 4 12 0 16" fill="none" stroke="var(--accent-blue)" stroke-width="1.5"/></svg>
          www.velvetpawvets.com
        </li>
      </ul>
      <div class="address">
        <svg width="14" height="20" viewBox="0 0 14 20" aria-hidden="true"><path d="M7 0a7 7 0 0 1 7 7c0 5-7 13-7 13S0 12 0 7a7 7 0 0 1 7-7z" fill="var(--accent-blue)"/><circle cx="7" cy="7" r="2.6" fill="var(--ink)"/></svg>
        <p>20947 E. 38th St<span>Scottsdale, AZ 85371</span></p>
      </div>
    </div>
  </section>
</body>
</html>
```